Updated brief for New ecommerce site needs a stunning business card that links to web site.

Updated business card brief. Please refer to the new files uploaded today (the last two) which show the background colour/style that we will be using in our web template for on-line trading, the grey marble concrete look.

Please see if you can use the grey marble background in the business card design in a way so it relates to our web template. It also needs to be transferable to banner ad, chatterbay ad etc.
brivo hub is a NEW eCommerce website which is commencing selling via tradlo & sellnook, used & damaged mobile phones & accessories, evolving into a full eCommerce store.

We like strong clean lines, use of a circle, in essence this will become our logo as well. Colours strong orange/Black/White The orange stronger than in CraftPanel #5352704 & grey marble as per file attached #153082

We love the use of a circle!! As we are evolving & moving forward this is what the circle represents to us……. ongoing change.

Front side with a circle with brivo hub in a modern font in the middle, brivo is in a strong orange and group is in black or white. On the reverse side, use layout as per Lumerax design from pelk.example. for icon details (not the boarder at top/botto).

This design is to meet www.pelk.example luxe cards specifications
Thank you we look forward to last minute inspiration.
Updates

Target Market(s)

Suppliers & business networking

Industry/Entity Type

Business

Contact Information for Business Card

Sam Ruiz
Director
mob +61 4987 6543
Locked Bag WXYZ 5678 QRS
sam@brivohub.example.au
www.brivohub.example.au

Requirements
Must have
• Design to meet www.pelk.example luxe business card specifications
• Colours - orange needs to be bold and strong & /black/white
• Circle with brivo hub in the middle
Nice to have
• Grey marble background incorporated into design in someway so it links with our web page.

```html
<!DOCTYPE html>
<html lang="en">
<head>
<meta charset="utf-8">
<title>brivohub business card</title>
<link rel="stylesheet" href="https://fonts.googleapis.com/css2?family=Nunito:wght@700;800&display=swap">
<style>
  :root {
    --brand-orange: #f05626;
    --brand-black: #000000;
    --brand-white: #ffffff;
    --canvas-grey: #d9d9d9;
    --card-shadow: rgba(0, 0, 0, 0.2);
  }
  * { margin: 0; padding: 0; box-sizing: border-box; }
  html, body {
    width: 1200px;
    height: 1000px;
    overflow: hidden;
    background: var(--canvas-grey);
    font-family: "Nunito", Arial, sans-serif;
  }
  .canvas {
    position: relative;
    width: 1200px;
    height: 1000px;
  }
  .card {
    position: absolute;
    width: 700px;
    height: 430px;
    box-shadow: 0 4px 14px var(--card-shadow);
  }
  .card--front {
    left: 60px;
    top: 50px;
    background: var(--brand-orange);
  }
  .card--back {
    left: 440px;
    top: 515px;
    background: var(--brand-black);
  }
  .front-circle {
    position: absolute;
    left: 50%;
    top: 50%;
    width: 350px;
    height: 350px;
    margin: -175px 0 0 -175px;
    border-radius: 50%;
    background: var(--brand-white);
    display: flex;
    align-items: center;
    justify-content: center;
  }
  .wordmark {
    font-weight: 800;
    letter-spacing: -0.5px;
    line-height: 1;
    white-space: nowrap;
  }
  .wordmark--front {
    font-size: 60px;
    color: var(--brand-orange);
  }
  .wordmark--back {
    position: absolute;
    left: 48px;
    top: 90px;
    font-size: 48px;
    color: var(--brand-white);
  }
  .contact {
    position: absolute;
    left: 384px;
    top: 236px;
    color: var(--brand-white);
    white-space: nowrap;
  }
  .contact__name {
    font-size: 27px;
    font-weight: 800;
    color: var(--brand-orange);
    margin-bottom: 16px;
  }
  .contact__line {
    font-size: 17px;
    font-weight: 700;
    margin-bottom: 16px;
  }
</style>
</head>
<body>
  <main class="canvas">
    <section class="card card--front" aria-label="Card front">
      <div class="front-circle">
        <span class="wordmark wordmark--front">brivohub</span>
      </div>
    </section>

    <section class="card card--back" aria-label="Card back">
      <span class="wordmark wordmark--back">brivohub</span>
      <div class="contact">
        <p class="contact__name">Nora Ellison</p>
        <p class="contact__line">nora@brivohub.example.au</p>
        <p class="contact__line">mob +61 400 555 019</p>
      </div>
    </section>
  </main>
</body>
</html>
```